Saucy Velvet Kittenz Business Card

We need business cards designed for our consultants to use and hand out to customers.
We are an Adult party plan company (like Crispaboxa but sex toys and lingerie)
We would like bright colours pinks, purples.
The cards need our logo
Space for the reps phone number email address and name.
We need our website on it www.saucyvelvetkittens.com.au

```html
<!DOCTYPE html>
<html lang="en">
<head>
<meta charset="utf-8">
<title>Saucy Velvet Kittenz Business Card</title>
<link rel="stylesheet" href="https://fonts.googleapis.com/css2?family=Dancing+Script:wght@500;700&family=Open+Sans:wght@400;600&display=swap">
<style>
  :root {
    --page-bg: #ece8ea;
    --pink-light: #e25bb5;
    --pink-base: #d42a9b;
    --pink-deep: #b8198a;
    --ink: #2a1a24;
    --black-card: #111012;
    --black-sheen: #2b2a2d;
    --logo-pink: #f04fb3;
    --silhouette: #1d1b1e;
  }
  * { margin: 0; padding: 0; box-sizing: border-box; }
  html, body { width: 1200px; height: 1014px; overflow: hidden; }
  body { background: var(--page-bg); position: relative; font-family: "Open Sans", sans-serif; }

  .card {
    position: absolute;
    width: 600px;
    height: 343px;
    border-radius: 4px;
    overflow: hidden;
    box-shadow: 0 10px 30px rgba(0,0,0,0.18);
  }

  /* Front: rep details */
  .card--front { left: 60px; top: 130px; }
  .front-backdrop {
    position: absolute;
    inset: 0;
    background: linear-gradient(135deg, var(--pink-light) 0%, var(--pink-base) 50%, var(--pink-deep) 100%);
  }
  .rep-figure {
    position: absolute;
    left: 30px; bottom: 0;
    width: 170px; height: 200px;
    background: linear-gradient(180deg, #2a2629, var(--silhouette));
    border-radius: 80px 80px 6px 6px;
  }
  .rep-name {
    position: absolute;
    left: 240px; top: 100px;
    font-family: "Dancing Script", cursive;
    font-weight: 500;
    font-size: 34px;
    line-height: 1.2;
    color: var(--ink);
  }
  .rep-title {
    position: absolute;
    left: 300px; top: 150px;
    font-size: 14px;
    color: var(--ink);
  }
  .rep-contact {
    position: absolute;
    left: 330px; bottom: 40px;
    font-size: 15px;
    line-height: 1.55;
    color: var(--ink);
  }

  /* Back: brand */
  .card--back {
    left: 540px; top: 560px;
    background: linear-gradient(160deg, var(--black-sheen) 0%, var(--black-card) 45%, var(--black-card) 100%);
  }
  .brand {
    position: absolute;
    left: 60px; top: 95px;
    display: flex; align-items: center; gap: 14px;
  }
  .brand-dot {
    width: 26px; height: 26px; border-radius: 50%;
    background: var(--logo-pink);
  }
  .brand-name {
    font-family: "Dancing Script", cursive;
    font-weight: 700;
    font-size: 42px;
    line-height: 1.2;
    color: var(--logo-pink);
    white-space: nowrap;
  }
  .brand-web {
    position: absolute;
    left: 110px; top: 215px;
    font-family: "Dancing Script", cursive;
    font-weight: 500;
    font-size: 26px;
    color: var(--logo-pink);
    white-space: nowrap;
  }
</style>
</head>
<body>
  <section class="card card--front">
    <div class="front-backdrop" role="img" aria-label="Decorative pink bokeh circle pattern"></div>
    <div class="rep-figure" role="img" aria-label="Silhouette illustration of a woman"></div>
    <div class="rep-name">Lena Marwood</div>
    <div class="rep-title">Manager</div>
    <div class="rep-contact">
      <div>phone: 555.014.2287</div>
      <div>lena@saucyvelvetkittens.com.au</div>
    </div>
  </section>

  <section class="card card--back">
    <div class="brand">
      <span class="brand-dot"></span>
      <span class="brand-name">Saucy Velvet Kittenz Parties</span>
    </div>
    <div class="brand-web">www.saucyvelvetkittens.com.au</div>
  </section>
</body>
</html>
```